Kestrel Electrical Business Card

We need a business card design for our family-run electrical contracting business based in Western Australia called 'Kestrel Electrical'. We provide electrical services including residential, commercial and industrial. We aim for individual business cards to be made for all of our employees. We already have a company logo, which we require to be featured on the design. We would like simple, sleek and vibrant designs, which incorporate our logo and represent our business. We do not want anything involving too many graphics/images. We like the colours red, black, white and all shades of grey. The final design should communicate professionalism and trustworthiness.
We require the following contact information:
Name- Owen Strickland
EC 5809
Mobile number- 0455 918 302
Fax number (including area code)- (08) 9640 2718
Email adress- name@kestrelelectrical.example
Electrical
- ITC Handel Bold

```html
<!DOCTYPE html>
<html lang="en">
<head>
<meta charset="utf-8">
<title>Kestrel Electrical Business Card</title>
<link rel="stylesheet" href="https://fonts.googleapis.com/css2?family=Michroma&family=Roboto:wght@300;400;700&family=Ubuntu:wght@500&display=swap">
<style>
  :root {
    --red: #e3191c;
    --black: #141414;
    --white: #f4f4f2;
    --grey-bg: #a9a9a9;
    --grey-text: #4a4a4a;
    --rule: #8a8a8a;
  }
  * { box-sizing: border-box; margin: 0; padding: 0; }
  html, body {
    width: 1200px; height: 720px; overflow: hidden;
    background: var(--grey-bg);
    font-family: "Roboto", Arial, sans-serif;
  }
  .stage {
    width: 1200px; height: 720px;
    display: flex; align-items: center; justify-content: center; gap: 40px;
  }
  .card {
    position: relative;
    width: 540px; height: 330px;
    overflow: hidden;
    box-shadow: 0 6px 18px rgba(0,0,0,.25);
  }
  .brand {
    display: flex; align-items: center; gap: 12px;
    font-family: "Michroma", "Arial Black", sans-serif;
    color: #fff; text-transform: uppercase;
    font-size: 22px; letter-spacing: 1px; line-height: 1;
  }
  .brand-mark { width: 20px; height: 20px; background: var(--white); flex: none; }

  /* Front */
  .card-front { background: var(--red); }
  .card-front .brand { position: absolute; left: 190px; top: 112px; }
  .card-front .brand-mark { background: #fff; }
  .front-band {
    position: absolute; left: 0; right: 0; top: 178px; height: 30px;
    background: var(--black);
    display: flex; align-items: center; justify-content: flex-end; padding-right: 40px;
  }
  .tagline {
    font-family: "Ubuntu", Arial, sans-serif; font-weight: 500;
    color: #fff; font-size: 13px; letter-spacing: 1px;
  }
  .tagline .sep { color: var(--red); margin: 0 5px; }

  /* Back */
  .card-back { background: var(--white); }
  .back-band {
    position: absolute; left: 0; right: 0; top: 0; height: 128px;
    background: var(--black);
  }
  .card-back .brand { position: absolute; left: 40px; top: 54px; }
  .card-back .brand-mark { background: var(--red); }
  .address {
    position: absolute; left: 40px; top: 152px; width: 250px;
    border-top: 1px solid var(--rule); padding-top: 10px;
    display: flex; gap: 8px;
    color: var(--grey-text); font-size: 13px; font-weight: 300; line-height: 1.3;
  }
  .address svg { flex: none; margin-top: 2px; }
  .contact {
    position: absolute; right: 40px; top: 196px; width: 260px;
    text-align: right; color: var(--grey-text);
  }
  .person-name { color: var(--red); font-weight: 700; font-size: 16px; }
  .person-role { font-size: 13px; font-weight: 400; padding-bottom: 6px; border-bottom: 1px solid var(--rule); margin-bottom: 6px; }
  .contact-line {
    display: flex; justify-content: flex-end; align-items: center; gap: 8px;
    font-size: 13px; font-weight: 300; line-height: 1.55;
  }
  .contact-line svg { flex: none; }
</style>
</head>
<body>
<main class="stage">
  <section class="card card-front" aria-label="Business card front">
    <div class="brand"><span class="brand-mark"></span><span>Kestrel Electrical</span></div>
    <div class="front-band">
      <p class="tagline">Residential<span class="sep">|</span>Industrial<span class="sep">|</span>Commercial</p>
    </div>
  </section>

  <section class="card card-back" aria-label="Business card back">
    <div class="back-band"></div>
    <div class="brand"><span class="brand-mark"></span><span>Kestrel Electrical</span></div>

    <div class="address">
      <svg width="10" height="14" viewBox="0 0 10 14" aria-hidden="true"><path d="M5 0a5 5 0 0 1 5 5c0 3.5-5 9-5 9S0 8.5 0 5a5 5 0 0 1 5-5z" fill="var(--red)"/><circle cx="5" cy="5" r="1.8" fill="#fff"/></svg>
      <p>EC 5809, address<br>town here 6542U</p>
    </div>

    <div class="contact">
      <p class="person-name">Owen Strickland</p>
      <p class="person-role">Director</p>
      <p class="contact-line">0455 918 302
        <svg width="12" height="12" viewBox="0 0 12 12" aria-hidden="true"><rect x="1" y="1" width="10" height="10" fill="none" stroke="var(--red)" stroke-width="1.6"/></svg>
      </p>
      <p class="contact-line">(08) 9640 2718
        <svg width="13" height="12" viewBox="0 0 13 12" aria-hidden="true"><rect x="3" y="0" width="7" height="4" fill="var(--red)"/><rect x="0" y="4" width="13" height="5" rx="1" fill="var(--red)"/><rect x="3" y="7" width="7" height="5" fill="#fff" stroke="var(--red)" stroke-width="1.2"/></svg>
      </p>
      <p class="contact-line">name@kestrelelectrical.example
        <svg width="13" height="10" viewBox="0 0 13 10" aria-hidden="true"><rect x="0" y="0" width="13" height="10" fill="var(--red)"/><path d="M0 0l6.5 5.5L13 0" fill="none" stroke="#fff" stroke-width="1.2"/></svg>
      </p>
    </div>
  </section>
</main>
</body>
</html>
```